Pawn & Gun store business card design

Hello! We would like a new business card design for our pawn & gun store. We loan money on items of value and sell firearms, jewelry, electronics & more.

Card will need to have the following information:

Business name - Prairie Nickel Pawn & Gun
Address - 2417 Hwy 41 S. Suite B Harlow Springs, OK 74061
Employees name - Marcus Pellen
Phone number - 972-555-0183
Email - PrairieNickelPawn@mailhaven.example
Website - PrairieNickelPawn.example

Somewhere on the card we would like it to say "Offering 10 Month Layaway!" & "We buy & loan on anything of value!". Our main store color is orange (please see logo). Logo does not have to be on the business card but it can be. Would like the back to have an area to write a note on the back. We like vintage things like old coins, collectables, firearms and more so think about this in the design. We want a business card as unique as our store!

Colors

Designer to choose colors to be used in the design.

Requirements
Nice to have
• Vintage Style

```html
<!DOCTYPE html>
<html lang="en">
<head>
<meta charset="utf-8">
<title>Prairie Nickel Pawn &amp; Gun — Business Card</title>
<link rel="stylesheet" href="https://fonts.googleapis.com/css2?family=Arvo:wght@700&family=Roboto:wght@400&family=Crimson+Text:wght@400;700&display=swap">
<style>
  :root {
    --backdrop: #ece4dc;
    --card: #fbfbfa;
    --orange: #c9561b;
    --brown: #3b2418;
    --grey: #555555;
    --shadow: rgba(60, 40, 25, 0.18);
  }
  * { box-sizing: border-box; margin: 0; padding: 0; }
  html, body { width: 1200px; height: 974px; overflow: hidden; }
  body { background: var(--backdrop); position: relative; }

  .card {
    position: absolute;
    top: 167px;
    width: 380px;
    height: 640px;
    background: var(--card);
    box-shadow: 0 6px 18px var(--shadow);
  }
  .card--front { left: 180px; padding: 66px 40px 56px; }
  .card--back { left: 640px; }

  .holder-name {
    font-family: "Arvo", Georgia, serif;
    font-weight: 700;
    font-size: 36px;
    line-height: 1.2;
    white-space: nowrap;
    color: var(--orange);
    letter-spacing: 0.5px;
  }
  .contact {
    position: absolute;
    left: 40px;
    right: 24px;
    bottom: 56px;
    font-family: "Roboto", Arial, sans-serif;
    font-size: 16px;
    line-height: 24px;
    color: var(--grey);
  }
  .contact__address { margin-bottom: 12px; }
  .contact__web { margin-top: 28px; color: var(--orange); font-size: 17px; }

  .brand {
    position: absolute;
    left: 0; right: 0;
    top: 330px;
    display: flex;
    align-items: center;
    justify-content: center;
    gap: 10px;
  }
  .brand__mark { width: 18px; height: 18px; background: var(--orange); }
  .brand__name {
    font-family: "Arvo", Georgia, serif;
    font-weight: 700;
    font-size: 24px;
    color: var(--orange);
  }

  .offer {
    position: absolute;
    left: 0; right: 0;
    top: 440px;
    text-align: center;
    font-family: "Crimson Text", Georgia, serif;
  }
  .offer__headline {
    font-weight: 700;
    font-size: 23px;
    letter-spacing: 0.5px;
    color: var(--brown);
    text-transform: uppercase;
  }
  .offer__tagline {
    display: flex;
    align-items: center;
    justify-content: center;
    gap: 8px;
    margin-top: 2px;
    font-size: 17px;
    color: var(--orange);
  }
  .offer__rule { width: 40px; height: 1px; background: var(--brown); }
</style>
</head>
<body>
  <section class="card card--front">
    <h1 class="holder-name">Marcus Pellen</h1>
    <div class="contact">
      <p class="contact__address">Prairie Nickel Pawn &amp; Gun<br>2417 Hwy 41 S.<br>Suite B Harlow Springs, OK 74061</p>
      <p class="contact__phone">P. 972-555-0183</p>
      <p class="contact__email">PrairieNickelPawn@mailhaven.example</p>
      <p class="contact__web">www.PrairieNickelPawn.example</p>
    </div>
  </section>

  <section class="card card--back">
    <div class="brand">
      <span class="brand__mark"></span>
      <span class="brand__name">Prairie Nickel Pawn</span>
    </div>
    <div class="offer">
      <p class="offer__headline">Offering 10 Month Layaway</p>
      <p class="offer__tagline"><span class="offer__rule"></span>We buy &amp; loan on anything of value<span class="offer__rule"></span></p>
    </div>
  </section>
</body>
</html>
```